Uncoded front page web design for wedding and event planning company

Hi.

I am launching a wedding and event planning company called Silver Fern Gatherings and need a professional and appealing web design.

So, let me explain my company. I am based in Swindon in Wiltshire but the company will plan weddings and events in Oxfordshire, Wiltshire, Berkshire and London.

We will plan weddings, birthdays, conferences, product launches, fashion shows and conventions but the main focus of the website at this stage should be the weddings with all the other occasions being covered under a single 'events' heading.

My contact details for the website should be:
Marion Blake
marion@silverferngatherings.co.uk
01632 960457 / 07700 900583

I'd like the website to feel clean, bright and elegant and be set against a white or off-white background. My logo is purple and I'd therefore like some purple incorporated into the design although feel free to use a more muted purple as my one might be a little bright? I'm also considering whether it would look nice paired with a little of the colour gold - maybe as a font colour in places?? I'll leave you to figure that one out as your design eye will be better than mine but for your reference below is my purple colour and my suggested gold one....

My purple colour is Pantone 2592 C but feel free to use others
My suggested gold I'm looking at is Pantone 14-1041 TCX

I would like to incorporate a Friendwall feed in the front page if possible, if it looks right. I'd also like to include a variety of pictures as well so I've included a few in a Dropbox folder which is linked below. Please don't feel obliged to use them all by any means (there's loads!) but you've got a few there to play with. If you find any other royalty free images you'd rather use please go ahead but on the understanding I can have them afterwards!

My logo can be retrieved via this Dropbox link...
You'll notice there are 2 styles of placement. Please feel free to use either to fit in with your design...
https://www.filedrawer-example.com/sh/qk7pa2mwx9rn4lt/BBBKzq8ohPnvve4S03LoPjvb?dl=0

The wedding images I have are in this Dropbox folder...
https://www.filedrawer-example.com/sh/m8wd6rzp2lo4ye1/BBB4kqrXv8nWd7S05JmOgtlp?dl=0

Other than that, it's over to you.... I can't wait to receive your designs :-)

Ooh....finally just to say, as I receive designs in I think I'll notice aspects that I like and don't like and if I feel they'll be useful for other designers, I'll update my brief below. Thanks

BRIEF UPDATE:
Someone asked if I had a tag-line. Could you use "Creating exquisite occasions today for amazing memories tomorrow"

I realise I hadn't explained what I'd like included on my home page so here's some notes to consider....

A welcome to section for me to start narrative about us and our services which has a button that links to our 'about us' page and 'services' page for further information.

A section that nicely illustrates what services we offer whether that be with icons or pictures.

A section with some photos in that would link to our gallery

A section that shows some customer reviews and blog entries that would link to my reviews page and blog to read more.

And finally a contact us section with my details, social media links and site map.

***
I also need to draw attention to where in the UK my services cover. I was therefore thinking perhaps we could use a picture to demonstrate this where it highlights Wiltshire, Oxfordshire, Berkshire and London on a map thereby demonstrating our areas covered. I have found several English county maps when searching on Google but I'm not sure how to highlight the areas I cover (or dull out the areas I don't) so if you have any ideas on this, I'd really like it incorporated. Thanks. (by the way, for those of you not familiar with English counties, the ones I cover are often abbreviated to Wilts, Oxon, Berks, London, so if you find a suitable map with those names on rather than the full names, you'll know what they are!)

I've found an image of the county map which might work well. I was wondering whether we might somehow grey out the counties I don't cover and just keep the ones I do as mentioned above and then crop it into perhaps a shadowed circle? I've attached a screenshot to the brief.
Updates

I've decided on the tag-line "Creating exquisite occasions today for amazing memories tomorrow" so if that could be included somewhere that would be great. I also need to draw attention to where in the UK my services cover. I was therefore thinking perhaps we could use a picture to demonstrate this where it highlights Wiltshire, Oxfordshire, Berkshire and London on a map thereby demonstrating our areas covered. I have found several English county maps when searching on Google but I'm not sure how to highlight the areas I cover (or dull out the areas I don't) so if you have any ideas on this, I'd really like it incorporated. Thanks. Added Wednesday, June 24, 2015

Target Market(s)

Predominately women aged 25-55

Industry/Entity Type

Wedding Planner

Number of Pages Required

1 page

Font styles to use
Sans Serif
Script

Requirements
Nice to have
• I'd like to see how the colour theme of purple and perhaps a little gold (maybe as a font colour) look against a white background. I've mentioned the Pantone colours in the brief above.
• I've attached a screenshot of a webpage with gold writing in and fonts that I like. Perhaps it could give you inspiration?
Should not have
• I really don't like the font QUILLORA so please done use that.

```html
<!DOCTYPE html>
<html lang="en">
<head>
<meta charset="utf-8">
<title>Silver Fern Gatherings — Wedding &amp; Event Planning</title>
<link rel="stylesheet" href="https://fonts.googleapis.com/css2?family=Playball&family=Noto+Serif:wght@400;700&display=swap">
<style>
:root{
  --purple:#7b0c98;
  --purple-title:#8a1aa6;
  --purple-bar:#8e1ba8;
  --gold:#f6d97c;
  --gold-edge:#e6c256;
  --gold-ink:#5a4a1a;
  --ink:#333;
  --body:#7a7a7a;
  --muted:#aaa;
  --page:#fff;
  --header-bg:#f4f3f3;
  --footer-bg:#efeded;
  --icon:#8e8e8e;
}
*{margin:0;padding:0;box-sizing:border-box}
html,body{width:1200px;height:2214px;overflow:hidden;background:var(--page)}
body{font-family:"Noto Serif",Georgia,serif;color:var(--ink);position:relative}
.script{font-family:"Playball",cursive;font-weight:400}

/* header */
.site-header{position:absolute;left:0;top:0;width:1200px;height:170px;background:var(--header-bg);border-bottom:8px solid var(--purple-bar)}
.brand{position:absolute;left:99px;top:62px;display:flex;align-items:center;gap:12px;font-size:25px;color:var(--purple);text-decoration:none}
.brand .dot{width:20px;height:20px;border-radius:50%;background:var(--purple)}
.contact-line{position:absolute;right:100px;top:46px;font-size:13px;color:#666;display:flex;align-items:center;gap:8px}
.contact-line svg{fill:var(--purple)}
.contact-line .sep{width:12px}
.main-nav{position:absolute;right:100px;top:106px;display:flex;font-size:15px}
.main-nav a{color:#666;text-decoration:none;margin-left:43px}
.main-nav a.active{color:var(--purple);font-weight:700}
.main-nav .caret{display:inline-block;margin-left:6px;border:5px solid transparent;border-top-color:#888;vertical-align:middle;transform:translateY(3px)}

/* hero */
.hero{position:absolute;left:0;top:170px;width:1200px;height:587px;
  background:
    radial-gradient(ellipse 180px 150px at 560px 150px,rgba(255,255,250,.95),rgba(255,255,250,0) 70%),
    radial-gradient(ellipse 140px 120px at 380px 170px,rgba(245,190,160,.9),rgba(245,190,160,0) 70%),
    radial-gradient(ellipse 110px 100px at 720px 340px,rgba(242,196,170,.9),rgba(242,196,170,0) 70%),
    radial-gradient(ellipse 120px 110px at 430px 470px,rgba(246,205,215,.95),rgba(246,205,215,0) 70%),
    radial-gradient(ellipse 70px 90px at 400px 530px,rgba(120,170,70,.85),rgba(120,170,70,0) 70%),
    radial-gradient(ellipse 140px 160px at 620px 330px,rgba(110,140,70,.55),rgba(110,140,70,0) 70%),
    linear-gradient(100deg,#b98d86 0%,#d9bdb2 22%,#efe2d6 45%,#f1e6d2 70%,#e5d8bd 88%,#4a3a30 100%)}
.hero-arrow{position:absolute;top:266px;width:48px;height:48px}
.hero-arrow.prev{left:41px}
.hero-arrow.next{right:41px}

/* welcome */
.welcome{position:absolute;left:0;top:757px;width:1200px;height:416px;background:#fff}
.welcome-photo{position:absolute;right:0;top:0;width:400px;height:416px;
  background:
    radial-gradient(ellipse 70px 90px at 110px 320px,rgba(170,150,200,.85),rgba(170,150,200,0) 70%),
    radial-gradient(ellipse 70px 90px at 250px 120px,rgba(120,80,50,.55),rgba(120,80,50,0) 70%),
    radial-gradient(ellipse 110px 150px at 260px 300px,rgba(250,248,244,1),rgba(250,248,244,0) 75%),
    radial-gradient(ellipse 60px 70px at 255px 190px,rgba(235,205,185,.9),rgba(235,205,185,0) 70%),
    linear-gradient(90deg,#fff 0%,#f3eeea 25%,#e8dcd3 60%,#f5f1ee 100%)}
.welcome h1{position:absolute;left:99px;top:84px;font-size:33px;line-height:1.2;color:var(--purple-title)}
.welcome .lead{position:absolute;left:99px;top:138px;font-size:17px;color:#444}
.welcome .copy{position:absolute;left:99px;top:189px;width:715px;font-size:12px;line-height:21.5px;color:var(--body)}
.btn{display:inline-block;background:var(--gold);border:1px solid var(--gold-edge);border-radius:20px;color:var(--gold-ink);font-size:12.5px;text-decoration:none;text-align:center}
.welcome .btn{position:absolute;left:99px;top:310px;width:110px;height:40px;line-height:38px}

/* events */
.events{position:absolute;left:0;top:1173px;width:1200px;height:417px;background:var(--purple)}
.events h2{position:absolute;left:99px;top:30px;font-size:32px;color:var(--gold)}
.events-arrows{position:absolute;right:98px;top:36px;display:flex;gap:7px}
.event-card{position:absolute;top:99px;width:227px}
.event-card .thumb{height:160px;border-radius:4px 4px 0 0}
.event-card h3{font-size:20px;color:#fff;margin:20px 0 6px;line-height:1.2}
.event-card p{font-size:12.5px;line-height:21px;color:#fff}
.event-card.featured{background:var(--gold);border-radius:4px;height:272px}
.event-card.featured .body{padding:0 16px}
.event-card.featured h3{color:#3a2400}
.event-card.featured p{color:#8a7a55}

/* lower */
.feed{position:absolute;left:99px;top:1636px;width:490px}
.about{position:absolute;left:648px;top:1636px;width:452px}
.feed h2,.about h2{font-size:32px;color:var(--purple-title);line-height:1}
.feed-item{position:absolute;left:0;width:490px}
.feed-item .thumb{position:absolute;left:0;top:4px;width:139px;height:112px;border-radius:3px}
.feed-item .date{position:absolute;left:168px;top:0;width:111px;height:26px;background:var(--gold);font-size:11.5px;font-weight:700;line-height:26px;padding-left:10px;color:#222}
.feed-item .text{position:absolute;left:168px;top:38px;width:320px;font-size:12.5px;line-height:21px;color:var(--body)}
.feed-item .meta{position:absolute;left:168px;top:110px;font-size:10.5px;color:var(--muted)}
.about .thumb{position:absolute;left:1px;top:79px;width:182px;height:137px;border-radius:3px}
.about .highlight{position:absolute;left:215px;top:90px;width:232px;font-size:12.5px;line-height:21px;color:var(--purple)}
.about .sub{position:absolute;left:215px;top:160px;width:232px;font-size:12.5px;line-height:21px;color:var(--body)}
.about .copy{position:absolute;left:1px;top:252px;width:452px;font-size:12.5px;line-height:21px;color:var(--body)}
.about .btn{position:absolute;left:1px;top:327px;width:111px;height:40px;line-height:38px}

/* footer */
.site-footer{position:absolute;left:0;top:2084px;width:1200px;height:130px;background:var(--footer-bg)}
.footer-nav{position:absolute;left:100px;top:42px;font-size:11px;color:#555}
.footer-nav a{color:#555;text-decoration:none}
.footer-nav span{margin:0 8px;color:#999}
.copyright{position:absolute;left:97px;top:75px;font-size:11.5px;color:#666}
.social{position:absolute;left:926px;top:47px;display:flex;gap:8px}
.social a{width:38px;height:38px;border-radius:50%;border:2px solid var(--icon);display:flex;align-items:center;justify-content:center}
.social svg{fill:var(--icon)}
</style>
</head>
<body>

<header class="site-header">
  <a class="brand" href="#"><span class="dot"></span>Silver Fern Gatherings</a>
  <div class="contact-line">
    <svg width="16" height="12" viewBox="0 0 16 12"><path d="M0 0h16v2L8 7 0 2z"/><path d="M0 4l8 5 8-5v8H0z"/></svg>
    <span>marion@silverferngatherings.co.uk</span>
    <span class="sep"></span>
    <svg width="12" height="14" viewBox="0 0 12 14"><path d="M2 0l3 3-1.5 2a8 8 0 0 0 4 5L9 8.5l3 3-2 2.5C5 13 0 8 0 2z"/></svg>
    <span>01632 960457 / 07700 900583</span>
  </div>
  <nav class="main-nav">
    <a class="active" href="#">Home</a>
    <a href="#">Weddings</a>
    <a href="#">Events<span class="caret"></span></a>
    <a href="#">Gallery</a>
    <a href="#">Contact</a>
  </nav>
</header>

<section class="hero" role="img" aria-label="Close-up of a bridal bouquet of white and peach roses tied with pink ribbon, resting on a wooden bench">
  <svg class="hero-arrow prev" viewBox="0 0 50 50"><circle cx="25" cy="25" r="22" fill="none" stroke="#fff" stroke-width="3"/><path d="M29 15L19 25l10 10" fill="none" stroke="#fff" stroke-width="4" stroke-linecap="round" stroke-linejoin="round"/></svg>
  <svg class="hero-arrow next" viewBox="0 0 50 50"><circle cx="25" cy="25" r="22" fill="none" stroke="#fff" stroke-width="3"/><path d="M21 15l10 10-10 10" fill="none" stroke="#fff" stroke-width="4" stroke-linecap="round" stroke-linejoin="round"/></svg>
</section>

<section class="welcome">
  <div class="welcome-photo" role="img" aria-label="Bride in a lace dress holding a bouquet of spring flowers"></div>
  <h1 class="script">Welcome to Silver Fern Gatherings</h1>
  <p class="lead">We are wedding and event planning company.</p>
  <p class="copy">Lorem ipsum dolor sit amet, consectetur adipiscing elit, sed do eiusmod tempor incididunt ut labore et dolore magna aliqua. Ut enim ad minim veniam, quis nostrud exercitation ullamco laboris nisi ut aliquip ex ea commodo consequat. Duis aute irure dolor in reprehenderit in voluptate velit esse cillum dolore eu fugiat nulla pariatur. Excepteur sint occaecat cupidatat non proident, sunt in culpa qui officia deserunt mollit anim id est laborum.</p>
  <a class="btn" href="#">Read More</a>
</section>

<section class="events">
  <h2 class="script">Our Events</h2>
  <div class="events-arrows">
    <svg width="32" height="32" viewBox="0 0 32 32"><circle cx="16" cy="16" r="14.5" fill="none" stroke="#fff" stroke-width="1.5"/><path d="M18 10l-6 6 6 6" fill="none" stroke="#fff" stroke-width="2"/></svg>
    <svg width="32" height="32" viewBox="0 0 32 32"><circle cx="16" cy="16" r="14.5" fill="none" stroke="#fff" stroke-width="1.5"/><path d="M14 10l6 6-6 6" fill="none" stroke="#fff" stroke-width="2"/></svg>
  </div>

  <article class="event-card featured" style="left:99px">
    <div class="thumb" role="img" aria-label="Couple exchanging rings beside a white bouquet" style="background:radial-gradient(ellipse 60px 50px at 140px 50px,#fbfaf5,rgba(251,250,245,0) 70%),radial-gradient(ellipse 50px 70px at 210px 110px,#2a2424,rgba(42,36,36,0) 75%),radial-gradient(ellipse 70px 50px at 80px 90px,#f0d8c8,rgba(240,216,200,0) 70%),linear-gradient(135deg,#c49a64,#e9dccb 55%,#cfc4b8)"></div>
    <div class="body">
      <h3 class="script">Wedding</h3>
      <p>Lorem ipsum dolor sit amnselo ctetur adipiscing eliteiu.</p>
    </div>
  </article>
  <article class="event-card" style="left:362px">
    <div class="thumb" role="img" aria-label="Young girls in white dresses at a garden party" style="background:radial-gradient(ellipse 40px 60px at 100px 110px,#f6f4ef,rgba(246,244,239,0) 75%),radial-gradient(ellipse 35px 55px at 30px 100px,#f2efe8,rgba(242,239,232,0) 75%),radial-gradient(ellipse 60px 60px at 170px 40px,#6a5a4a,rgba(106,90,74,0) 75%),linear-gradient(135deg,#4f6e30,#7f9a4e 50%,#5d7038)"></div>
    <h3 class="script">Birthdays</h3>
    <p>Lorem ipsum dolor sit amet, conselo ctetur adipiscing elit, sed deiu.</p>
  </article>
  <article class="event-card" style="left:617px">
    <div class="thumb" role="img" aria-label="Conference hall set with white-draped tables and chairs" style="background:radial-gradient(ellipse 30px 45px at 113px 30px,#26402a,rgba(38,64,42,0) 80%),radial-gradient(ellipse 90px 40px at 113px 120px,#fbfaf7,rgba(251,250,247,0) 80%),linear-gradient(90deg,#a8935e,#e5ddc6 25%,#ece7da 75%,#a8935e)"></div>
    <h3 class="script">Conferences</h3>
    <p>Lorem ipsum dolor sit amet, conselo ctetur adipiscing elit, sed deiu.</p>
  </article>
  <article class="event-card" style="left:874px">
    <div class="thumb" role="img" aria-label="Waiter serving plated canapés at a launch reception" style="background:radial-gradient(ellipse 60px 30px at 100px 100px,#fbfbf9,rgba(251,251,249,0) 80%),radial-gradient(ellipse 50px 25px at 160px 50px,#f7f6f2,rgba(247,246,242,0) 80%),radial-gradient(ellipse 40px 40px at 205px 120px,#e3b89a,rgba(227,184,154,0) 80%),linear-gradient(135deg,#7d6f62,#d8cfc6 50%,#b9a48e)"></div>
    <h3 class="script">Product Launches</h3>
    <p>Lorem ipsum dolor sit amet, conselo ctetur adipiscing elit, sed deiu.</p>
  </article>
</section>

<section class="feed">
  <h2 class="script">Friendwall Feed</h2>
  <article class="feed-item" style="top:79px">
    <div class="thumb" role="img" aria-label="Bride and guests among white lilies at a ceremony" style="background:radial-gradient(ellipse 35px 45px at 35px 70px,#f4f1e8,rgba(244,241,232,0) 75%),radial-gradient(ellipse 30px 50px at 110px 60px,#fafafa,rgba(250,250,250,0) 75%),linear-gradient(135deg,#55683a,#b8ad94 50%,#ddd4c6)"></div>
    <div class="date">June 23 2015</div>
    <p class="text">Lorem ipsum dolor sit amet, consectetur adipiscing elit, sed do eiusmod tempor incididunt ut labore et dolore magna aliquntenim ad minim veniam.</p>
    <p class="meta">0 Comments &nbsp;|&nbsp; 34 Likes</p>
  </article>
  <article class="feed-item" style="top:246px">
    <div class="thumb" role="img" aria-label="Evening reception tables with tall purple floral centrepieces" style="background:radial-gradient(ellipse 40px 30px at 70px 40px,#b49ad8,rgba(180,154,216,0) 75%),radial-gradient(ellipse 70px 25px at 70px 95px,#e7e6f2,rgba(231,230,242,0) 80%),linear-gradient(180deg,#1a1d38,#44386e 55%,#8c84b4)"></div>
    <div class="date">June 23 2015</div>
    <p class="text">Lorem ipsum dolor sit amet, consectetur adipiscing elit, sed do eiusmod tempor incididunt ut labore et dolore magna aliquntenim ad minim veniam.</p>
    <p class="meta">0 Comments &nbsp;|&nbsp; 34 Likes</p>
  </article>
</section>

<section class="about">
  <h2 class="script">About Our Event Planning</h2>
  <div class="thumb" role="img" aria-label="Bouquet of pink orchids and roses" style="background:radial-gradient(ellipse 40px 35px at 60px 60px,#f3a8c0,rgba(243,168,192,0) 75%),radial-gradient(ellipse 40px 35px at 130px 80px,#f5b8b0,rgba(245,184,176,0) 75%),radial-gradient(ellipse 30px 25px at 95px 35px,#9aa85a,rgba(154,168,90,0) 75%),radial-gradient(circle at 50% 50%,#d9789c,#e49ab2 55%,#f4e6e9)"></div>
  <p class="highlight">Lorem ipsum dolor sit amet, consectetur adipiscing elit, sed do eiusmod tempor incididunt ut labore</p>
  <p class="sub">At dolore magna aliquntenim adminim veniam.quis nostrud exercitation ull amco lorem ispum dolor.</p>
  <p class="copy">Lorem ipsum dolor sit amet, consectetur adipiscing elit, sed do eiusmod tempor incididunt ut labore et dolore magna aliquntenim ad minim</p>
  <a class="btn" href="#">Read More</a>
</section>

<footer class="site-footer">
  <nav class="footer-nav">
    <a href="#">Home</a><span>|</span><a href="#">Weddings</a><span>|</span><a href="#">Events</a><span>|</span><a href="#">Gallery</a><span>|</span><a href="#">Contact</a>
  </nav>
  <p class="copyright">Copyright © 2015 &nbsp;All Rights Reserved.silverferngatherings. Tems and conditions</p>
  <div class="social" aria-label="Social media links">
    <a href="#" aria-label="Chat with us"><svg width="16" height="14" viewBox="0 0 16 14"><path d="M2 0h12a2 2 0 0 1 2 2v7a2 2 0 0 1-2 2H7l-4 3v-3H2a2 2 0 0 1-2-2V2a2 2 0 0 1 2-2z"/></svg></a>
    <a href="#" aria-label="Share"><svg width="15" height="15" viewBox="0 0 15 15"><circle cx="12" cy="3" r="2.5"/><circle cx="3" cy="7.5" r="2.5"/><circle cx="12" cy="12" r="2.5"/><path d="M3 7.5L12 3M3 7.5L12 12" stroke="#8e8e8e" stroke-width="1.4" fill="none"/></svg></a>
    <a href="#" aria-label="Favourites"><svg width="16" height="14" viewBox="0 0 16 14"><path d="M8 14L1.5 7.5A4 4 0 0 1 8 2.2a4 4 0 0 1 6.5 5.3z"/></svg></a>
    <a href="#" aria-label="Email us"><svg width="16" height="12" viewBox="0 0 16 12"><path d="M0 0h16v2L8 7 0 2z"/><path d="M0 4l8 5 8-5v8H0z"/></svg></a>
  </div>
</footer>

</body>
</html>
```